Vellum Systemics Buisness Cards

I need a technology focused clean business card for my employees. I have attached out logo to include in the mocks. We're a modern tech consulting firm that drives to interface humanity with technology in a truly cohesive fashion.

```html
<!DOCTYPE html>
<html lang="en">
<head>
<meta charset="utf-8">
<title>Vellum Systemics – Business Cards</title>
<link rel="stylesheet" href="https://fonts.googleapis.com/css2?family=Arimo:wght@400;700&display=swap">
<style>
  :root {
    --backdrop: #7a4524;
    --kraft-light: #dcb98f;
    --kraft-mid: #cfa677;
    --kraft-dark: #bf915f;
    --ink: #111111;
  }
  * { margin: 0; padding: 0; box-sizing: border-box; }
  html, body { width: 1200px; height: 900px; overflow: hidden; }
  body {
    position: relative;
    background: var(--backdrop);
    font-family: "Arimo", Arial, sans-serif;
    color: var(--ink);
  }
  .card {
    position: absolute;
    left: 330px;
    width: 556px;
    height: 343px;
    background: linear-gradient(135deg, var(--kraft-light) 0%, var(--kraft-mid) 45%, var(--kraft-dark) 100%);
    box-shadow: 3px 4px 8px rgba(0,0,0,0.45);
  }
  .card--front { top: 90px; }
  .card--back { top: 470px; width: 558px; }

  .contact {
    position: absolute;
    left: 0; right: 0;
    top: 64px;
    text-align: center;
    font-size: 15.5px;
    line-height: 20px;
    margin-left: -2px;
  }
  .contact__name { font-weight: 700; font-size: 17.5px; letter-spacing: 0.3px; }
  .contact__title { font-size: 15.5px; }
  .contact__rule {
    width: 196px;
    height: 1px;
    background: var(--ink);
    margin: 11px auto 12px;
  }
  .contact__label { font-weight: 700; }
  .contact__address { margin-top: 18px; }

  .brand {
    position: absolute;
    left: 0; right: 0;
    top: 50%;
    transform: translateY(-50%);
    display: flex;
    align-items: center;
    justify-content: center;
    gap: 14px;
    margin-left: -10px;
  }
  .brand__mark {
    width: 58px; height: 58px;
    border-radius: 50%;
    border: 7px solid var(--ink);
  }
  .brand__name {
    font-weight: 700;
    font-size: 34px;
    letter-spacing: 1px;
    text-transform: uppercase;
  }
</style>
</head>
<body>
  <section class="card card--front" aria-label="Business card front">
    <div class="contact">
      <p class="contact__name">MARCUS ELLERY</p>
      <p class="contact__title">Managing Director</p>
      <div class="contact__rule"></div>
      <p><span class="contact__label">P:</span> 044-210 555 0148</p>
      <p><span class="contact__label">M:</span> 044-210 555 0148</p>
      <p><span class="contact__label">E:</span> info@vellumsys.com</p>
      <p><span class="contact__label">W:</span> www.vellumsys.com</p>
      <div class="contact__rule"></div>
      <p class="contact__address">48 Harrow Lane, Suite 5<br>Northgate, 204817.</p>
    </div>
  </section>

  <section class="card card--back" aria-label="Business card back">
    <div class="brand">
      <span class="brand__mark" aria-hidden="true"></span>
      <span class="brand__name">Vellum Systemics</span>
    </div>
  </section>
</body>
</html>
```